STATIONERY and Brand ID for Tralven

We need a family of identical Brand guide
Call Card
Envelope
Letterhead
Poster
Brochure

It needs to have an international Fee/

The ARCHITECTURE/STRUCTURE must show the highest level of creativity

1. Call card could be two sided
2. cal card can have a a flap
3. Call card can have a curved edge

Target Market(s)

Business and bank clients

Industry/Entity Type

Bank

Requirements
Must have
• the logo atatched
• the colour scheme must be used
• There must be a common look and feel and they must have the same DNA

```html
<!DOCTYPE html>
<html lang="en">
<head>
<meta charset="utf-8">
<title>Tralven Call Card</title>
<link href="https://fonts.googleapis.com/css2?family=Questrial&family=Montserrat:wght@700&display=swap" rel="stylesheet">
<style>
  :root {
    --navy: #062a72;
    --green: #6cb41a;
    --paper: #f7f8fa;
    --ink: #3a3f4a;
    --stage: #e4e4ef;
  }
  * { margin: 0; padding: 0; box-sizing: border-box; }
  html, body { width: 1200px; height: 906px; overflow: hidden; background: var(--stage); }
  body { font-family: "Questrial", sans-serif; position: relative; }

  .card {
    position: absolute; left: 290px; width: 620px; height: 354px;
    border-radius: 4px; overflow: hidden;
    box-shadow: 0 6px 18px rgba(40, 40, 90, 0.18);
  }
  .card-back { top: 70px; background: var(--navy); }
  .card-front { top: 482px; background: var(--paper); }

  .wordmark { display: flex; align-items: center; gap: 12px; position: absolute; }
  .wordmark-dot { width: 16px; height: 16px; border-radius: 50%; background: var(--green); }
  .wordmark-name { font-family: "Montserrat", sans-serif; font-weight: 700; font-size: 44px; letter-spacing: -1px; line-height: 1; }

  .card-back .wordmark { left: 50%; top: 150px; transform: translateX(-50%); }
  .card-back .wordmark-name { color: #ffffff; }
  .back-web { position: absolute; right: 40px; bottom: 34px; color: #ffffff; font-size: 15px; letter-spacing: 0.5px; }

  .card-front .wordmark { right: 40px; top: 44px; }
  .card-front .wordmark-name { color: var(--navy); font-size: 40px; }

  .holder { position: absolute; left: 40px; top: 132px; }
  .holder-name { font-family: "Montserrat", sans-serif; font-weight: 700; color: var(--navy); font-size: 19px; letter-spacing: 0.5px; }
  .holder-role { color: var(--ink); font-size: 15px; margin-top: 2px; }

  .address { position: absolute; right: 40px; top: 136px; text-align: right; color: var(--ink); font-size: 15px; line-height: 1.35; font-style: normal; }

  .contacts { position: absolute; left: 40px; bottom: 52px; list-style: none; color: var(--ink); font-size: 14px; }
  .contacts li { display: flex; align-items: center; gap: 9px; line-height: 19px; }
  .contact-icon { width: 14px; height: 14px; flex: none; }

  .edge-band { position: absolute; left: 0; bottom: 0; width: 620px; height: 30px; }
</style>
</head>
<body>

<section class="card card-back" aria-label="Card back">
  <div class="wordmark">
    <span class="wordmark-dot"></span>
    <span class="wordmark-name">Tralven</span>
  </div>
  <p class="back-web">www.tralven.bank</p>
</section>

<section class="card card-front" aria-label="Card front">
  <div class="wordmark">
    <span class="wordmark-dot"></span>
    <span class="wordmark-name">Tralven</span>
  </div>

  <div class="holder">
    <h1 class="holder-name">ALDER RENSHAW</h1>
    <p class="holder-role">General Manager - Saint Lucia</p>
  </div>

  <address class="address">
    # 7 Harbour Lane<br>P O Box 2740<br>Port Ellery<br>Saint Lucia
  </address>

  <ul class="contacts">
    <li>
      <svg class="contact-icon" viewBox="0 0 14 14"><rect width="14" height="14" rx="2" fill="#062a72"/><path d="M4 3.5c.6-.4 1.2 0 1.4.6l.4 1.1c.1.4-.1.7-.4.9l-.4.3c.5 1 1.2 1.7 2.2 2.2l.3-.4c.2-.3.5-.5.9-.4l1.1.4c.6.2 1 .8.6 1.4-.6.9-1.6 1.1-2.6.6C5.8 9.3 4.7 8.2 3.9 6.6c-.5-1-.3-2.3.1-3.1z" fill="#fff"/></svg>
      +17580142200
    </li>
    <li>
      <svg class="contact-icon" viewBox="0 0 14 14"><rect width="14" height="14" rx="2" fill="#062a72"/><rect x="4.5" y="2.5" width="5" height="9" rx="1" fill="none" stroke="#fff" stroke-width="1.2"/></svg>
      +17580142233
    </li>
    <li>
      <svg class="contact-icon" viewBox="0 0 14 14"><rect width="14" height="14" rx="2" fill="#062a72"/><rect x="3" y="4" width="8" height="6" fill="none" stroke="#fff" stroke-width="1.1"/><path d="M3 4l4 3.2L11 4" fill="none" stroke="#fff" stroke-width="1.1"/></svg>
      alderrenshaw@tralven.bank
    </li>
    <li>
      <svg class="contact-icon" viewBox="0 0 14 14"><rect width="14" height="14" rx="2" fill="#062a72"/><circle cx="7" cy="7" r="4" fill="none" stroke="#fff" stroke-width="1"/><ellipse cx="7" cy="7" rx="1.8" ry="4" fill="none" stroke="#fff" stroke-width="0.9"/><path d="M3 7h8" stroke="#fff" stroke-width="0.9"/></svg>
      www.tralven.bank
    </li>
  </ul>

  <svg class="edge-band" viewBox="0 0 620 30" preserveAspectRatio="none" aria-hidden="true">
    <polygon points="0,20 330,20 326,30 0,30" fill="#062a72"/>
    <polygon points="346,12 620,0 620,30 336,30" fill="#6cb41a"/>
  </svg>
</section>

</body>
</html>
```